Brivane - Business Cards for a new venture

create business card for a startup classified business dealing in construction materials, the cards need to have a professional look but modern, more serious than playful, one of the samples must include the official font (attached), please explore using the official colors in the company's logo

Target Market(s)

Energy sector

Contact Information for Business Card

Font styles to use
Other font styles liked:
• suissnord

Requirements
Must have
• corporate colors (in logo attached)
Nice to have
• Official font (in one of the samples) font is : suissnord
Should not have
• Cartoonish look

```html
<!DOCTYPE html>
<html lang="en">
<head>
<meta charset="utf-8">
<title>Brivane Business Cards</title>
<link rel="stylesheet" href="https://fonts.googleapis.com/css2?family=Open+Sans:wght@400;700&display=swap">
<style>
  :root {
    --backdrop: #212121;
    --card: #ffffff;
    --navy: #134a82;
    --steel: #97989c;
    --ink: #3d3d3d;
  }
  * { box-sizing: border-box; margin: 0; padding: 0; }
  html, body { width: 1200px; height: 1200px; overflow: hidden; }
  body {
    background: var(--backdrop);
    font-family: "Open Sans", Arial, sans-serif;
    position: relative;
  }
  .card {
    position: absolute;
    left: 170px;
    width: 842px;
    height: 480px;
    background: var(--card);
    overflow: hidden;
  }
  .card--front { top: 98px; }
  .card--back { top: 620px; }
  .card__band {
    position: absolute;
    left: 0; right: 0; bottom: 0;
    height: 12px;
    border-top: 5px solid var(--steel);
    background: var(--navy);
  }
  .brand {
    position: absolute;
    display: flex;
    align-items: center;
    gap: 14px;
    transform: translateX(-50%);
  }
  .brand__mark {
    width: 22px; height: 22px;
    background: var(--navy);
  }
  .brand__name {
    color: var(--steel);
    font-weight: 400;
    letter-spacing: 0.22em;
    text-transform: uppercase;
    line-height: 1;
  }
  .card--front .brand { left: 421px; top: 215px; }
  .card--front .brand__name { font-size: 44px; }
  .card--back .brand { left: 656px; top: 170px; }
  .card--back .brand__name { font-size: 34px; }
  .card--back .brand__mark { width: 18px; height: 18px; }

  .person {
    position: absolute;
    left: 52px; top: 70px;
  }
  .person__name {
    color: var(--navy);
    font-weight: 700;
    font-size: 27px;
    letter-spacing: 0.08em;
    line-height: 1;
  }
  .person__role {
    color: var(--ink);
    font-size: 15px;
    letter-spacing: 0.12em;
    margin-top: 10px;
  }
  .person__email {
    color: var(--navy);
    font-size: 18px;
    margin-top: 28px;
  }
  .person__rule {
    width: 345px;
    height: 2px;
    background: var(--navy);
    margin-top: 18px;
  }
  .contact {
    position: absolute;
    left: 60px;
    color: var(--ink);
    font-size: 18px;
    display: flex;
    align-items: center;
    gap: 10px;
  }
  .contact svg { flex: none; }
  .contact--phone { top: 336px; }
  .contact--office { top: 336px; left: 252px; }
  .contact--address { top: 379px; }
</style>
</head>
<body>
  <section class="card card--front">
    <div class="brand">
      <span class="brand__mark"></span>
      <span class="brand__name">Brivane</span>
    </div>
    <div class="card__band"></div>
  </section>

  <section class="card card--back">
    <div class="person">
      <h1 class="person__name">DANIEL CARVER</h1>
      <p class="person__role">ASSOCIATE MANAGER</p>
      <p class="person__email">danielcarver@brivane.co</p>
      <div class="person__rule"></div>
    </div>

    <div class="brand">
      <span class="brand__mark"></span>
      <span class="brand__name">Brivane</span>
    </div>

    <div class="contact contact--phone">
      <svg width="14" height="24" viewBox="0 0 14 24" aria-hidden="true">
        <rect x="1" y="1" width="12" height="22" rx="2" fill="none" stroke="var(--navy)" stroke-width="1.6"/>
        <line x1="5" y1="19.5" x2="9" y2="19.5" stroke="var(--navy)" stroke-width="1.6"/>
      </svg>
      <span>+62-614208735</span>
    </div>

    <div class="contact contact--office">
      <svg width="18" height="18" viewBox="0 0 18 18" aria-hidden="true">
        <rect x="1" y="1" width="16" height="16" fill="none" stroke="var(--navy)" stroke-width="1.4"/>
        <g fill="var(--navy)">
          <rect x="4" y="4" width="2" height="2"/><rect x="8" y="4" width="2" height="2"/><rect x="12" y="4" width="2" height="2"/>
          <rect x="4" y="8" width="2" height="2"/><rect x="8" y="8" width="2" height="2"/><rect x="12" y="8" width="2" height="2"/>
          <rect x="7" y="12" width="4" height="5"/>
        </g>
      </svg>
      <span>Head office New York</span>
    </div>

    <div class="contact contact--address">
      <svg width="16" height="20" viewBox="0 0 16 20" aria-hidden="true">
        <path d="M8 1a5 5 0 0 1 5 5c0 4-5 8-5 8s-5-4-5-8a5 5 0 0 1 5-5z" fill="none" stroke="var(--navy)" stroke-width="1.4"/>
        <circle cx="8" cy="6" r="1.8" fill="none" stroke="var(--navy)" stroke-width="1.3"/>
        <path d="M3 14l-2 5h14l-2-5" fill="none" stroke="var(--navy)" stroke-width="1.3"/>
      </svg>
      <span>48/2 Harlow Street, Ridgeway Park, New York, United States, 351204</span>
    </div>

    <div class="card__band"></div>
  </section>
</body>
</html>
```